The Hollowreed Project WEBSITE DESIGN

Hollowreed is a not for profit working in international aid and development. The website needs to be lively not depressing,earthy rather than bling, have a dramatic impact over lightweight. It may be that a black and white with spot colour may be more impacting given the simplicity I want for the site. Hollowreed works in partnership with registered NGOs in Asia and Africa. At any one time it will have about five feature projects. The purpose is for people to be able to find out about the projects, the countries, the partner organisations, people's stories and then give people the opportunity to give their financial and volunteer support.

Target Market(s)

First World Donors
All ages but particularly 25 - 55

Industry/Entity Type

Human Rights

Number of Pages Required

5+ page

Font styles to use
Sans Serif

Requirements
Must have
• Simplicity
• Easy access to giving options
• Highlight stories both video and image + copy (sample in attachments)
• Lots of images over copy
Nice to have
• Interest
• Not boring
• May work in black and white with a spot colour or sepia look
Should not have
• Shiny new look
• Dont know how many pages or if it be coded or uncoded - makes no sense to me

```html
<!DOCTYPE html>
<html lang="en">
<head>
<meta charset="utf-8">
<title>The Hollowreed Project</title>
<link rel="stylesheet" href="https://fonts.googleapis.com/css2?family=Raleway:wght@400;500;600&family=Roboto+Slab:wght@400&family=Open+Sans:wght@400;600&display=swap">
<style>
:root{
  --orange:#ee8f00;
  --orange-light:#f7a21a;
  --orange-dark:#e07f00;
  --blue:#2a9fd6;
  --blue-band-top:#62b2de;
  --blue-band-bottom:#3f8fcf;
  --ink:#3a3a3a;
  --muted:#7a7a7a;
  --footer:#f2f2f2;
  --white:#ffffff;
}
*{margin:0;padding:0;box-sizing:border-box}
html,body{width:769px;height:1200px;overflow:hidden;background:var(--white)}
body{position:relative;font-family:"Open Sans",Arial,sans-serif;color:var(--ink)}
.abs{position:absolute}

.site-header{position:absolute;left:0;top:0;width:769px;height:73px;background:var(--white)}
.brand{position:absolute;left:0;right:0;top:24px;display:flex;justify-content:center;align-items:center;gap:9px}
.brand-mark{width:30px;height:30px;border-radius:50%;background:var(--orange)}
.brand-name{font-family:"Raleway",sans-serif;font-weight:600;font-size:20px;color:var(--blue);letter-spacing:.3px}

.main-nav{position:absolute;left:0;top:73px;width:769px;height:28px;background:linear-gradient(var(--orange-light),var(--orange-dark))}
.nav-item{position:absolute;top:0;height:28px;display:flex;align-items:center;gap:5px;font-family:"Raleway",sans-serif;font-weight:600;font-size:9.6px;color:var(--white);border-right:1px solid rgba(255,255,255,.25);padding-left:0;justify-content:center}
.nav-item svg{width:14px;height:14px}
.nav-item.giving{background:#e37c00;border-right:none}

.hero{position:absolute;left:0;top:101px;width:769px;height:305px;background:linear-gradient(180deg,#c9d9c4 0%,#7f9a5e 35%,#d8c25a 70%,#9b7a45 100%)}
.hero-quote{position:absolute;left:108px;top:160px;font-family:"Roboto Slab",serif;font-size:28px;line-height:30px}
.hero-quote .line-one{color:var(--blue)}
.hero-quote .line-two{color:var(--orange);padding-left:22px}
.hero-quote .mark{font-size:34px}
.slider-dots{position:absolute;left:351px;top:282px;display:flex;gap:4px}
.slider-dots span{width:13px;height:13px;border-radius:50%;background:var(--white)}
.slider-dots span.active{background:var(--blue)}

.about{position:absolute;left:0;top:436px;width:769px;text-align:center}
.section-title{font-family:"Raleway",sans-serif;font-weight:400;font-size:22px;color:var(--ink)}
.about-lead{margin:14px auto 0;width:480px;font-size:7.8px;line-height:10.5px;color:#555}
.about-body{margin:8px auto 0;width:470px;font-size:6px;line-height:10.6px;color:var(--muted)}

.story-col{position:absolute;top:570px;width:250px}
.col-title{font-family:"Raleway",sans-serif;font-size:15px;color:var(--orange)}
.story-card{display:flex;margin-top:9px;gap:14px}
.thumb{flex:none;width:68px;height:53px;position:relative}
.play{position:absolute;left:50%;top:50%;width:17px;height:17px;margin:-8.5px 0 0 -8.5px;border-radius:50%;background:var(--white)}
.play::after{content:"";position:absolute;left:6.5px;top:4.5px;border-left:6px solid #222;border-top:4px solid transparent;border-bottom:4px solid transparent}
.story-name{font-size:8px;color:#444;margin-top:-1px}
.story-text{font-size:5.4px;line-height:10.5px;color:#777;margin-top:2px}
.read-more{font-size:6px;color:var(--blue);margin-top:2px}

.projects{position:absolute;left:0;top:684px;width:769px;height:161px;background:linear-gradient(var(--blue-band-top),var(--blue-band-bottom))}
.projects .section-title{position:absolute;left:0;right:0;top:26px;text-align:center;color:var(--white);font-size:17px}
.project{position:absolute;top:68px;display:flex;gap:6px;width:150px}
.project-icon{flex:none;width:24px;height:24px;border-radius:50%;border:2px solid var(--white);margin-top:1px}
.project-name{font-family:"Raleway",sans-serif;font-size:12px;color:var(--white)}
.project-text{font-size:6px;line-height:10.3px;color:#e8f3fb;margin-top:1px}

.watch{position:absolute;left:137px;top:876px}
.watch-title{font-family:"Raleway",sans-serif;font-size:15px;color:var(--blue)}
.video-thumb{position:absolute;top:29px;width:119px;height:68px}

.cta{position:absolute;left:0;top:1007px;width:769px;height:121px;background:var(--orange);text-align:center}
.cta-title{margin-top:27px;font-family:"Raleway",sans-serif;font-size:17px;color:var(--white)}
.cta-text{margin:8px auto 0;width:450px;font-size:7.5px;line-height:10.8px;color:#fde3bc}

.site-footer{position:absolute;left:0;top:1128px;width:769px;height:72px;background:var(--footer)}
.footer-links{position:absolute;left:140px;top:22px;font-size:8px;color:#333}
.footer-links .sep{margin:0 4px}
.footer-links .small{font-size:6.5px}
.copyright{position:absolute;left:140px;top:39px;font-size:6px;color:#999}
.social{position:absolute;left:571px;top:22px;display:flex;gap:6px}
.social span{width:11px;height:11px;border-radius:50%;background:#444}
</style>
</head>
<body>

<header class="site-header">
  <div class="brand">
    <span class="brand-mark"></span>
    <span class="brand-name">HOLLOWREED PROJECT</span>
  </div>
</header>

<nav class="main-nav">
  <div class="nav-item" style="left:146px;width:110px">
    <svg viewBox="0 0 14 14"><circle cx="7" cy="7" r="6.5" fill="#fff"/><text x="7" y="10.5" text-anchor="middle" font-size="10" font-weight="700" fill="#ee8f00" font-family="Arial,sans-serif">?</text></svg>ABOUT HOLLOWREED
  </div>
  <div class="nav-item" style="left:256px;width:109px">
    <svg viewBox="0 0 14 14"><circle cx="7" cy="4" r="3" fill="#fff"/><path d="M1 14c0-4 3-6 6-6s6 2 6 6z" fill="#fff"/></svg>LIVE PROJECTS
  </div>
  <div class="nav-item" style="left:365px;width:108px">
    <svg viewBox="0 0 14 14"><rect x="1" y="4" width="12" height="9" fill="none" stroke="#fff" stroke-width="1.4"/><rect x="5" y="1.5" width="4" height="2.5" fill="none" stroke="#fff" stroke-width="1.2"/></svg>OUR STORIES
  </div>
  <div class="nav-item" style="left:473px;width:79px">
    <svg viewBox="0 0 14 14"><rect x="1" y="3" width="12" height="9" fill="#fff"/><path d="M1 3l6 5 6-5" fill="none" stroke="#ee8f00" stroke-width="1.2"/></svg>CONTACT
  </div>
  <div class="nav-item giving" style="left:552px;width:83px">
    <svg viewBox="0 0 14 14"><path d="M7 12.5L1.8 7.3A3 3 0 0 1 7 3.2a3 3 0 0 1 5.2 4.1z" fill="none" stroke="#fff" stroke-width="1.4"/></svg>GIVING
  </div>
</nav>

<section class="hero" role="img" aria-label="Photograph of three smiling women and a young child standing in a green rural field">
  <div class="hero-quote">
    <div class="line-one"><span class="mark">“</span>People have dreams,</div>
    <div class="line-two">People have capacity<span class="mark">”</span></div>
  </div>
  <div class="slider-dots"><span class="active"></span><span></span><span></span><span></span></div>
</section>

<section class="about">
  <h2 class="section-title">About Hollowreed</h2>
  <p class="about-lead">arcu Morbi porta libero id ullamcorper nonummy nibh ligula pulvinar metus eget consectetuer augue nisi quis lacus Ut ac mi quis lacus mollis aliquam Curabitur iaculis tempus eros</p>
  <p class="about-body">magna malesuada ultrices Ut nisi erat fermentum vel congue id euismod in elit Fusce ultricies orci ac feugiat suscipit leo massa sodales velit et scelerisque mi tortor at ipsum cligula augue bibendum accumsan vestibulum ut commodo a mi Morbi ornare gravida elit Integer congue augue et malesuada iaculis ipsum dui aliquet felis at cursus magna nisl nec elit Praesent elementum elit at tellus nec ultricies sit amet porttitor mattis enim In massa libero interdum nec interdum vel blandit sed nulla In ullamcorper est eget tempor cursus neque mi consectetuer mi</p>
</section>

<div class="story-col" style="left:136px">
  <h3 class="col-title">The Hollowreed Story</h3>
  <div class="story-card">
    <div class="thumb" role="img" aria-label="Video still of a man with bunches of green bananas beside a road" style="background:linear-gradient(135deg,#6e8a3a,#b9a26a)"><span class="play"></span></div>
    <div>
      <div class="story-name">Marisol’s Story</div>
      <p class="story-text">Before joining SHG, I was a miserable poor isolated housewife. I didn’t know that one could save very little and enable to earn much</p>
      <div class="read-more">READ MORE</div>
    </div>
  </div>
</div>

<div class="story-col" style="left:390px">
  <h3 class="col-title">Our Stories</h3>
  <div class="story-card">
    <div class="thumb" role="img" aria-label="Photograph of a woman's feet and colourful patterned skirt" style="background:linear-gradient(135deg,#d9a23a,#c4a57a)"></div>
    <div>
      <div class="story-name">Consolata’s Story</div>
      <p class="story-text">I joined the groups in 2013. Before joining the group, women couldn’t attend meetings. I was isolated doing housework</p>
      <div class="read-more">READ MORE</div>
    </div>
  </div>
</div>

<section class="projects">
  <h2 class="section-title">Our Projects</h2>
  <div class="project" style="left:160px">
    <span class="project-icon"></span>
    <div><div class="project-name">Lotus Path Cambodia</div><p class="project-text">widow’s silk weaving cooperative; children’s home; rural schools project (building toilets and updating buildings falling into disrepair)</p></div>
  </div>
  <div class="project" style="left:335px;width:130px">
    <span class="project-icon"></span>
    <div><div class="project-name">Hillside Rwanda</div><p class="project-text">women’s self help groups in rural Rwanda</p></div>
  </div>
  <div class="project" style="left:501px;width:145px">
    <span class="project-icon"></span>
    <div><div class="project-name">Wellstone Kenya</div><p class="project-text">coaching women NGO leaders from around the country</p></div>
  </div>
</section>

<section class="watch">
  <h2 class="watch-title">Watch Our Stories</h2>
  <div class="video-thumb" style="left:1px;background:linear-gradient(135deg,#a0583a,#d49a6a)" role="img" aria-label="Video still of two women in front of a brick wall"><span class="play"></span></div>
  <div class="video-thumb" style="left:128px;background:linear-gradient(135deg,#8a7256,#c9b08a)" role="img" aria-label="Video still of women and a child at a doorway"><span class="play"></span></div>
  <div class="video-thumb" style="left:255px;background:linear-gradient(135deg,#4c4f4a,#8a8a80)" role="img" aria-label="Video still of a classroom with a chalkboard"><span class="play"></span></div>
  <div class="video-thumb" style="left:380px;background:linear-gradient(135deg,#4a3a2e,#8c7460)" role="img" aria-label="Video still of three men standing in a workshop"><span class="play"></span></div>
</section>

<section class="cta">
  <h2 class="cta-title">Duis sed tellus et tortor vestibulum</h2>
  <p class="cta-text">Maecenas aliquet velit vel turpis Mauris neque metus malesuada nec ultricies sit amet porttitor mattis enim In massa libero interdum nec interdum vel blandit sed nulla In ullamcorper est eget tempor cursus neque mi consectetuer mi a ultricies massa est sed nisl Class aptent taciti sociosqu ad litora torquent per</p>
</section>

<footer class="site-footer">
  <div class="footer-links">About Hollowreed<span class="sep">|</span>Live Projects<span class="sep">|</span>Storyboard<span class="sep">|</span>Giving<span class="sep">|</span><span class="small">Contact</span></div>
  <div class="copyright">© 2015 Company Name &nbsp;All right reserved &nbsp;Term of Use</div>
  <div class="social"><span></span><span></span><span></span><span></span></div>
</footer>

</body>
</html>
```